Brand Business Card for Hotel Cloud Management System

Hello designers,
we are looking for a new brand business card for our product Stayvora. Our brand Stayvora is a hotel management system for small hotels, B&B, guesthouses etc. and just recently we are expanding our offer to other European markets. Therefore we need a business card that will communicate not only to the end-users (hoteliers) but also to potential business partners/ We would like the brand business card to be professional looking, but not too serius, modern, elegant, clean, Our brand color is orange, dark grey and it would be nice to see both combined.

Please visit our website www.stayvora.eu to get more impression on what our brand stayvora stands for.

Please find attached stayvora logo.

Target Market(s)

small hotels, hoteliers, B&B owners, potential business partners

Industry/Entity Type

Software Service

Contact Information for Business Card

Stayvora
- hotel software solutions - web booking engine - multi channel manager
www.stayvora.eu
T: +38614738265
E: info@stayvora.net

Font styles to use
Serif
Sans Serif

Colors
f37122
aaaaaa
606060
f6f6f6

Requirements
Must have
• Logo of the brand
• the layout of the business card should be in connection with the look and feel of the website stayvora.eu and logo stayvora;

```html
<!DOCTYPE html>
<html lang="en">
<head>
<meta charset="utf-8">
<title>Stayvora – Business Card</title>
<link href="https://fonts.googleapis.com/css2?family=Open+Sans:wght@400;600;700;800&display=swap" rel="stylesheet">
<style>
  :root {
    --orange: #f37122;
    --orange-deep: #e8621a;
    --grey-dark: #606060;
    --grey-mid: #aaaaaa;
    --paper: #f6f6f6;
    --white: #ffffff;
    --ink: #1f1f1f;
    --backdrop: #2a2c2f;
  }
  * { box-sizing: border-box; margin: 0; padding: 0; }
  html, body {
    width: 1200px; height: 900px; overflow: hidden;
    background: var(--backdrop);
    font-family: "Open Sans", Arial, sans-serif;
  }
  .sheet {
    position: relative; width: 1200px; height: 900px;
    display: flex; align-items: center; justify-content: center; gap: 60px;
  }
  .card {
    position: relative; width: 510px; height: 300px;
    border-radius: 4px; overflow: hidden;
  }

  /* Contact side */
  .card--contact { background: var(--paper); }
  .contact-icons {
    position: absolute; left: 40px; top: 36px;
    display: flex; flex-direction: column; gap: 24px;
  }
  .contact-icons svg { width: 18px; height: 18px; display: block; }
  .contact-rule {
    position: absolute; left: 82px; top: 30px;
    width: 2px; height: 122px; background: var(--orange);
  }
  .contact-list {
    position: absolute; left: 104px; top: 34px;
    list-style: none; color: var(--grey-dark);
    font-size: 15px; line-height: 1.2;
  }
  .contact-list li + li { margin-top: 22px; }
  .brand-mark {
    position: absolute; right: 36px; top: 120px;
    display: flex; align-items: center; gap: 12px;
  }
  .brand-mark__square {
    width: 46px; height: 46px; border-radius: 6px; background: var(--orange);
  }
  .brand-mark__name {
    font-size: 30px; font-weight: 700; color: var(--orange); letter-spacing: -0.5px;
  }
  .service-band {
    position: absolute; left: 0; right: 0; bottom: 0; height: 44px;
    background: var(--grey-dark); color: var(--white);
    display: flex; align-items: center; padding-left: 22px;
    font-size: 13.5px; letter-spacing: 0.2px;
  }
  .service-band__notch {
    position: absolute; top: -6px; left: 250px;
    width: 14px; height: 7px; background: var(--grey-dark);
    border-radius: 7px 7px 0 0;
  }
  .service-band .sep { margin: 0 8px; color: var(--grey-mid); }

  /* Brand side */
  .card--brand { background: var(--orange); }
  .brand-disc {
    position: absolute; left: 120px; top: 26px;
    width: 248px; height: 248px; border-radius: 50%;
    background: var(--paper);
    display: flex; flex-direction: column; align-items: center; justify-content: center;
  }
  .brand-disc__name {
    font-size: 42px; font-weight: 800; color: var(--ink); letter-spacing: -1px; line-height: 1;
  }
  .brand-disc__tagline {
    margin-top: 8px; font-size: 13px; color: var(--ink); letter-spacing: 0.3px;
  }
</style>
</head>
<body>
<main class="sheet">

  <section class="card card--contact" aria-label="Business card, contact side">
    <div class="contact-icons" aria-hidden="true">
      <svg viewBox="0 0 24 24"><path fill="#606060" d="M6.6 10.8c1.4 2.8 3.8 5.1 6.6 6.6l2.2-2.2c.3-.3.7-.4 1-.2 1.1.4 2.3.6 3.6.6.6 0 1 .4 1 1V20c0 .6-.4 1-1 1C10.6 21 3 13.4 3 4c0-.6.4-1 1-1h3.5c.6 0 1 .4 1 1 0 1.3.2 2.5.6 3.6.1.3 0 .7-.2 1z"/></svg>
      <svg viewBox="0 0 24 24"><rect x="2" y="5" width="20" height="14" rx="1" fill="#606060"/><path d="M2.5 5.5 12 13l9.5-7.5" fill="none" stroke="#f6f6f6" stroke-width="1.5"/></svg>
      <svg viewBox="0 0 24 24"><g fill="none" stroke="#606060" stroke-width="1.8"><circle cx="12" cy="12" r="9"/><ellipse cx="12" cy="12" rx="4" ry="9"/><path d="M3 12h18M5 7h14M5 17h14"/></g></svg>
    </div>
    <div class="contact-rule"></div>
    <ul class="contact-list">
      <li>+38 614 738 265</li>
      <li>info@stayvora.net</li>
      <li>www.stayvora.eu</li>
    </ul>
    <div class="brand-mark">
      <span class="brand-mark__square" aria-hidden="true"></span>
      <span class="brand-mark__name">Stayvora</span>
    </div>
    <div class="service-band">
      <span class="service-band__notch" aria-hidden="true"></span>
      Hotel Software Solutions<span class="sep">|</span>Web Booking Engine<span class="sep">|</span>Multi Channel Manager
    </div>
  </section>

  <section class="card card--brand" aria-label="Business card, brand side">
    <div class="brand-disc">
      <span class="brand-disc__name">Stayvora</span>
      <span class="brand-disc__tagline">hotel pms service</span>
    </div>
  </section>

</main>
</body>
</html>
```